website design + images

We need a very appealing website design, layout and images for a sales analytics and sales productivity services company based in San Ramon, California. We need a good design for the home page and a template for all other pages (total 2 designs), and images for all inner pages (center column/banner images, and right hand top corner small images). There are about 18 inner pages.
Updates

Our existing website is www.vorlaxen.com
Our corporate colours are the ones that are there on the website. The logo is also shown. We will be changing the tagline to "accelerating revenue" or equivalent of that.

Please use the document "website for vorlaxen - template v2.doc" that I just uploaded for any reference to the content, navigation and wireframes. A few more clarifications are provided mainly for the link "Solutions".

Devendra Kothuri

Hi,
We just uploaded ver 4 of the website template. There is more elaboration provided around the sublinks / sections for Solutions. Pls review and do get back if you need any clarifications.

Rgds
Devendra Kothuri

Hi all,
We have so far received a few good designs. The designs are more or less on the right track. I would like to urge all of you to use the content and navigation provided in the document attached to our brief "website for vorlaxen - template v4.doc".  Please DO NOT use the content in our existing website www.vorlaxen.com . That is very old. We mentioned it only for reference to colour theme and broad details.

We have totally 13 sections in Solutions pages. They may be designed as a tree of links - first level sublinks - second level sublinks or links - first level sublinks and the remaining as sections within the first level sublinks pages. The page design would remain the same for all inner pages except careers. But after finalizing the design for the inner page, we will need images for the different inner pages.

Rgds
Devendra Kothuri

Hi,
Thank you all for participation and very good designs. We are quite happy with what we have seen. We have now shortlisted about 4 vendors and sending invididual feedback to them for further improvement. We will be finalizing by Monday or Tuesday.  To the vendors who do not get feedback from us, thank you very much for participation. We may still do business in future for some of our other needs. 
The following are the process steps / expectations going forward, 
1. Feedback to the shortlisted designers and inviting improvements.
2. Review of the improved designs and further shortlist & feedback or direct finalization.
3. The design should be in 1024*768
2. Number of page designs = 2 (home page, inner page).
4. Home page design: instead of delivery model and customers, show one link "Why Us".
4. Solutions page design:  We will be needing an image in center column of solutions page that in a nutshell gives all the different types of solutions we provide. The entire set of solutions is in our attached document website for vorlaxen - template v4 and I am just uploading v5 with more description on sublinks.
5. After selection, we will be needing images for all the solution pages (total 12 pages under solutions + one solutions page), 1 image for Why Us?, 1 for Careers, and 3 for company (about us/ team, core values, ...) = total 18

Rgds
Devendra Kothuri

Target Market(s)

We are a sales analytics and sales productivity services company. We help B2B companies with: sales planning; sales operations and sales measurement. The characteristics of our customers are:
- B2B medium enterprises (USD 100M- USD 2B in revenue) in the US
- Primary target verticals are: high-tech, engineering and professional services firms
- Our primary target customers titles are VP of Sales or VP of marketing; we could be selling to the CEO at companies with revenues below $200M

Industry/Entity Type

Consulting

Requirements
Must have
• - Clean, uncluttered design
• - Easy navigation; minimum clicks
Nice to have
• We have already built a content management system and wireframes for this site. To the extent possible, it would be great to leverage the wireframe structure we built, provided you don’t have to compromise on the look and feel and navigation of the site. Below is what we currently have as banner sizes and resolutions are:
• Home page banner size: 950 * 250’
• All pages – center top - image size: 558 * 160
• All pages – right hand top image – 175*135’

```html
<!DOCTYPE html>
<html lang="en">
<head>
<meta charset="utf-8">
<title>Vorlaxen – Careers</title>
<link rel="stylesheet" href="https://fonts.googleapis.com/css2?family=Noto+Sans:wght@400;600&family=PT+Sans:wght@400;700&display=swap">
<style>
:root{
  --ink:#222;
  --muted:#666;
  --teal:#1aaba8;
  --orange:#e05a16;
  --link:#1d3f7a;
  --band-top:#3b7cca;
  --band-bottom:#8fb9e9;
  --panel-border:#c9cdd3;
  --tab-top:#ffffff;
  --tab-bottom:#e3e6ea;
  --footer-top:#8dbcf0;
  --footer-bottom:#6fa3e6;
  --leaf:#4a9a2a;
}
*{box-sizing:border-box;margin:0;padding:0}
html,body{width:1200px;height:517px;overflow:hidden}
body{position:relative;background:#fbfbfd;font-family:"Noto Sans",Verdana,sans-serif;color:var(--ink);font-size:11px}
.page-backdrop{position:absolute;inset:0;background:
  radial-gradient(ellipse 260px 420px at 40px 200px,rgba(120,165,225,.18),transparent 70%),
  radial-gradient(ellipse 260px 420px at 1160px 200px,rgba(120,165,225,.18),transparent 70%),
  linear-gradient(#f3f4f6 0,#fff 77px)}
.header-band{position:absolute;left:0;top:78px;width:1200px;height:114px;background:linear-gradient(var(--band-top),var(--band-bottom));box-shadow:0 3px 4px rgba(0,0,0,.15)}
.brand{position:absolute;left:222px;top:22px;display:flex;align-items:center;gap:8px;font-family:"PT Sans",sans-serif;font-size:26px;letter-spacing:2px;color:#1d5aa0}
.brand-dot{width:14px;height:14px;border-radius:50%;background:#1d5aa0}
.utility-links{position:absolute;left:818px;top:5px;display:flex;align-items:center;gap:5px;font-size:11px;color:#0a2a5a}
.main-nav{position:absolute;left:417px;top:50px;display:flex;gap:3px}
.main-nav a{display:block;height:25px;line-height:25px;text-align:center;font-size:13px;color:#111;text-decoration:none;background:linear-gradient(var(--tab-top),var(--tab-bottom));border:1px solid #d4d7db;border-bottom:none}
.main-nav a.is-active{color:#1d5aa0}
.panel{position:absolute;background:#fff;border:1px solid var(--panel-border);border-radius:5px}
.side-nav{left:206px;top:78px;width:146px;height:342px;padding-top:13px;list-style:none;background:rgba(255,255,255,.92)}
.side-nav li{display:flex;align-items:center;font-size:11px;color:#111}
.side-nav .top{height:21px;padding-left:11px}
.side-nav .top::before{content:"";width:5px;height:7px;margin-right:9px;background:radial-gradient(circle,#888 1px,transparent 1.2px) 0 0/3px 3px}
.side-nav .sub{height:25px;padding-left:23px}
.side-nav .sub::before{content:"···›";margin-right:4px;color:var(--leaf);font-weight:600;letter-spacing:-1px}
.banner{left:358px;top:78px;width:482px;height:114px;overflow:hidden;border-radius:5px;border:1px solid #cfe0f3;background:linear-gradient(90deg,#c7dcf2,#e9f2fb 45%,#d3e5f7)}
.banner-photo{position:absolute;left:0;top:0;width:160px;height:114px;background:linear-gradient(135deg,#d8e4ef,#c7a98c 55%,#e7edf3)}
.banner-card{position:absolute;left:162px;top:12px;width:309px;height:81px;background:#fff;border-radius:8px;box-shadow:0 1px 3px rgba(0,0,0,.15);padding:9px 0 0 32px}
.banner-card h1{font-family:"PT Sans",sans-serif;font-weight:700;font-size:19px;color:var(--teal);line-height:22px}
.banner-card p{margin-top:5px;padding-left:7px;color:var(--muted);line-height:15px;width:240px}
.corner-photo{left:848px;top:78px;width:145px;height:114px;overflow:hidden;background:linear-gradient(135deg,#f2f5f9,#c9d6e4 60%,#eef2f6)}
.corner-photo p{position:absolute;left:26px;top:65px;line-height:15px;color:#111}
.content{left:358px;top:205px;width:482px;height:215px;padding:10px 16px}
.content h2{font-family:"PT Sans",sans-serif;font-weight:700;font-size:15px;color:var(--teal);line-height:18px}
.content p{line-height:16.7px;color:#333;width:460px}
.content p+p{margin-top:10px}
.aside{left:848px;top:205px;width:145px;height:215px;padding:7px 8px}
.aside h3{font-family:"PT Sans",sans-serif;font-weight:400;font-size:15px;color:var(--orange);border-left:4px solid var(--orange);padding-left:8px;line-height:15px;margin-left:1px}
.aside-photo{margin-top:8px;width:131px;height:80px;border-radius:4px;background:linear-gradient(90deg,#e8c8ae,#efe9e5 50%,#d6d8dc)}
.aside p{margin-top:11px;line-height:14px;color:#333}
.aside .read-more{position:absolute;right:7px;bottom:8px;color:var(--link)}
.site-footer{position:absolute;left:6px;top:429px;width:1194px;height:67px;border-radius:5px 0 0 5px;background:linear-gradient(var(--footer-top),var(--footer-bottom));display:flex;align-items:center;justify-content:center;color:#111}
</style>
</head>
<body>
<div class="page-backdrop"></div>
<div class="header-band"></div>

<div class="brand"><span class="brand-dot"></span>VORLAXEN</div>

<div class="utility-links">
  <svg width="20" height="20" viewBox="0 0 20 20" aria-hidden="true"><circle cx="8" cy="8" r="5.5" fill="#e8f0f8" stroke="#555" stroke-width="1.6"/><line x1="12" y1="12" x2="18" y2="18" stroke="#333" stroke-width="2.6" stroke-linecap="round"/></svg>
  <span>Sign in</span><span>|</span><span>Contact us</span><span>|</span><span>Sitemap</span>
</div>

<nav class="main-nav">
  <a class="is-active" style="width:88px">Home</a>
  <a style="width:88px">Solutions</a>
  <a style="width:120px">Delivery Model</a>
  <a style="width:88px">Customers</a>
  <a style="width:88px">Company</a>
  <a style="width:88px">Careers</a>
</nav>

<ul class="panel side-nav">
  <li class="top">Home</li>
  <li class="top">Solutions</li>
  <li class="sub">Managed Services</li>
  <li class="sub">Consulting</li>
  <li class="sub">Contract Staffing</li>
  <li class="top">Delivery Model</li>
  <li class="top">Customers</li>
  <li class="top">Company</li>
  <li class="sub">About Us</li>
  <li class="sub">Our Culture &amp; Values</li>
  <li class="sub">Philanthropy</li>
  <li class="sub">Careers</li>
  <li class="sub">Contact Us</li>
  <li class="top">Careers</li>
</ul>

<div class="panel banner">
  <div class="banner-photo" role="img" aria-label="Photo of a smiling professional woman in an office"></div>
  <div class="banner-card">
    <h1>Careers</h1>
    <p>Lorem Ipsum is simply dummy text of the printing and typesetting industry.</p>
  </div>
</div>

<div class="panel corner-photo" role="img" aria-label="Photo of a team of colleagues in a meeting">
  <p>Lorem Ipsum is simply dummy text of the printing and</p>
</div>

<main class="panel content">
  <h2>Careers</h2>
  <p>We are an employee-focused company consisting of passionate individuals who work hard and play hard. Do you want to be the best at what you do? Do you thrive in chal&shy;lenging, fast-paced environments? Do you consider continuous learning and a passion for excellence two of your driving forces? If so, let’s talk. Our doors are always open to exceptional individuals.</p>
  <p>Join our team. Learn, contribute, and make a difference. Be appreciated and rewarded.</p>
</main>

<aside class="panel aside">
  <h3>Consulting</h3>
  <div class="aside-photo" role="img" aria-label="Photo of a support consultant wearing a headset"></div>
  <p>Vorlaxen delivers cus&shy;tomized solutions to address your biggest marketing and sales operations challenges.</p>
  <span class="read-more">Read more...</span>
</aside>

<footer class="site-footer">© 2010 Vorlaxen, Inc. | Contact Us | Sign in (register) | Contact us | Sitemap</footer>
</body>
</html>
```